Gadgetpickerhelp.com needs your creativity!

We need a website design for a new internet company based in Winnipeg MB called gadgetpickerhelp.com. We provide customers who are relatively new to technology a professional intermediary in the computer buying process. We act as an independent purchasing assistant for our customers by getting a clear understanding of their needs and requirements of their machine and proceed to find a computer with the exact specifications they require at the lowest possible price. Because we are completely independent we do not push any particular brand, OS, or software. We want the website to be bold but streamlined, it should be easy to use and navigate even for a beginner.

Target Market(s)

45+ age bracket

Industry/Entity Type

Internet

Requirements
Must have
• The site must have an About Us page, as well as a secure shopping cart where customers can purchase the service via paylinko and credit card. In this section we will require all of the customer's information to be entered as well as what their needs are for their new computer
I would like a product comparison chart that is broken down into three columns where the features of each service can be checked or unchecked depending on each package. I also need an extended service page, where customers will be able to contact me or directly purchase a remote servicing package
Nice to have
• I would like to have an introductory video for the service provided available to customers on the home page so one click and they will be able to see what our service is about.
Should not have
• Do not use any loud audio or sound clips in the design, subtle sound is fine.

```html
<!DOCTYPE html>
<html lang="en">
<head>
<meta charset="utf-8">
<title>Gadget Picker Help</title>
<link href="https://fonts.googleapis.com/css2?family=Open+Sans:wght@400;600;700&family=Michroma&display=swap" rel="stylesheet">
<style>
:root{
  --teal:#1aa9b8;
  --teal-dark:#0f8c9a;
  --logo-red:#e0482a;
  --ink:#333;
  --muted:#666;
  --page:#f5f2ee;
  --footer:#ebe9e7;
  --rule:#cfcac4;
  --card:#fff;
  --photo-a:#b89a86;
  --photo-b:#d9cfc6;
  --screen-a:#1f5ea8;
  --screen-b:#0d3e7a;
}
*{box-sizing:border-box;margin:0;padding:0}
html,body{width:834px;height:1200px;overflow:hidden}
body{background:var(--page);font-family:"Open Sans",Arial,sans-serif;color:var(--ink);position:relative}
.abs{position:absolute}

.logo{left:75px;top:14px;font-size:22px;font-weight:700;color:var(--logo-red);letter-spacing:.2px;white-space:nowrap}
.cart{left:538px;top:17px;display:flex;align-items:center;gap:6px}
.cart-select{width:66px;height:17px;border:1px solid #ccc;background:#fff;font-size:9px;color:#999;padding:2px 4px;position:relative;white-space:nowrap}
.cart-select::after{content:"";position:absolute;right:4px;top:6px;border:4px solid transparent;border-top:5px solid #b32;}
.social{left:652px;top:20px;display:flex;gap:8px}
.social span{width:22px;height:22px;border-radius:50%;background:#3b4a5a;display:block}
.social span:nth-child(2){background:#f4f4f4;border:1px solid #ccc}
.social span:nth-child(3){background:#2c4762}
.social span:nth-child(4){background:#2a8a3a}

.nav{left:0;top:54px;width:834px;height:25px;background:linear-gradient(#f3f3f3,#dcdcdc);border-top:1px solid #d0d0d0}
.nav ul{list-style:none;display:flex;gap:15px;margin-left:78px;line-height:25px;font-size:12px;color:#333;white-space:nowrap}
.search{left:0;top:79px;width:834px;height:30px;background:linear-gradient(var(--teal),var(--teal-dark))}
.search-label{left:74px;top:79px;width:112px;height:30px;background:var(--teal-dark);color:#fff;font-size:13px;line-height:30px;padding-left:4px;white-space:nowrap}
.select{top:84px;height:21px;background:#eee;border:1px solid #ccc;font-size:8.5px;color:#555;line-height:19px;padding-left:5px;white-space:nowrap}
.select::after{content:"";position:absolute;right:5px;top:6px;border:5px solid transparent;border-top:8px solid #666;border-bottom:0}

.slider-shadow{left:74px;top:110px;width:686px;height:252px;background:#fbfaf8;box-shadow:0 2px 6px rgba(0,0,0,.08)}
.hero{left:98px;top:124px;width:471px;height:230px;background:linear-gradient(135deg,var(--photo-b),var(--photo-a) 60%,#8f7868)}
.featured{left:88px;top:143px;width:108px;height:19px;background:var(--teal);color:#fff;font-weight:700;font-size:13px;line-height:19px;padding-left:19px;white-space:nowrap}
.dots{left:472px;top:314px;display:flex;gap:2px}
.dots span{width:10px;height:10px;background:#e05a1c;color:#fff;font-size:7px;text-align:center;line-height:10px}
.special{left:569px;width:173px;height:57px;color:#fff;padding:7px 7px}
.special h3{font-family:"Michroma",sans-serif;font-size:7.6px;font-weight:400;color:#0b3b40;letter-spacing:.6px;margin-bottom:6px;white-space:nowrap}
.special p{font-size:7px;line-height:11px}

.heading{left:75px;height:24px;background:var(--teal);color:#fff;font-size:15px;line-height:24px;padding:0 11px;white-space:nowrap}
.heading-rule{left:188px;width:320px;height:1px;background:var(--rule)}
.card{width:101px;height:104px;background:var(--card);border:3px solid #e6e2de}
.card .shot{position:absolute;left:10px;top:15px;width:76px;height:62px;background:linear-gradient(var(--screen-a),var(--screen-b));border:3px solid #222;border-bottom-width:4px}
.card .base{position:absolute;left:2px;top:80px;width:92px;height:6px;background:linear-gradient(#cfd3d8,#8d939a);border-radius:0 0 3px 3px}
.meta{font-size:10px;color:var(--teal-dark);line-height:15.5px}

.side-h{left:544px;font-size:11.5px;font-weight:700;color:var(--teal);white-space:nowrap}
.side-bar{left:544px;width:210px;height:4px;background:#e2ded9}
.specs{left:544px;top:418px;display:grid;grid-template-columns:119px 90px;font-size:9px;line-height:20.8px;color:#333;white-space:nowrap}
.post{left:546px;width:208px}
.post .thumb{position:absolute;left:0;top:0;width:56px;height:56px;background:#ddd;border:1px solid #e8e8e8}
.post p{margin-left:67px;font-size:7.8px;line-height:11.8px;color:#444;text-align:justify}
.post-rule{left:546px;width:208px;height:1px;background:#bbb}

.footer{left:0;top:1030px;width:834px;height:138px;background:var(--footer)}
.foot-h{font-size:14px;font-weight:700;color:var(--teal)}
.about-p{left:83px;top:1071px;width:203px;font-size:8px;line-height:14px;color:#666;text-align:justify}
.links{font-size:8px;line-height:14px;color:#666;white-space:nowrap}
.pay{left:588px;top:1083px;width:160px;height:56px;background:#e0e5ea;border-radius:3px}
.pay small{position:absolute;right:6px;top:4px;font-size:7px;color:#888}
.pay .badges{position:absolute;left:5px;top:20px;display:flex;gap:3px}
.pay .badges span{height:18px;background:#fff;border:1px solid #ccc;font-size:6.5px;color:#24476f;line-height:16px;padding:0 3px;white-space:nowrap}
.copy{left:84px;top:1181px;font-size:8px;color:#555;white-space:nowrap}
</style>
</head>
<body>
<div class="abs logo">Gadget Picker Help</div>

<div class="abs cart">
  <svg width="30" height="28" viewBox="0 0 30 28" aria-hidden="true"><path d="M2 4h5l4 14h14l3-10H9" fill="none" stroke="#888" stroke-width="2"/><circle cx="12" cy="23" r="2.3" fill="#888"/><circle cx="23" cy="23" r="2.3" fill="#888"/></svg>
  <div class="cart-select">Add to cart</div>
</div>
<div class="abs social" aria-label="Social links"><span></span><span></span><span></span><span></span></div>

<nav class="abs nav"><ul><li>About Us</li><li>Exceptional Value</li><li>Package Extended</li><li>Service Package</li><li>Full Service Package</li><li>FAQs</li><li>Testimonials</li><li>Contact Us</li></ul></nav>
<div class="abs search"></div>
<div class="abs search-label">Search by choice</div>
<div class="abs select" style="left:193px;width:148px">Select Category</div>
<div class="abs select" style="left:348px;width:148px">Select Brand</div>
<div class="abs select" style="left:502px;width:128px">Select Type</div>
<div class="abs select" style="left:637px;width:128px">Select Price</div>

<div class="abs slider-shadow"></div>
<div class="abs hero" role="img" aria-label="Featured photo: shopper resting among a laptop, boxes and gadgets"></div>
<div class="abs featured">FEATURED</div>
<div class="abs dots"><span>2</span><span>3</span></div>
<div class="abs special" style="top:124px;background:#1a9eae"><h3>THIS WEEK'S SPECIAL</h3><p>Lorem ipsum dolor sit amet, consectetur adipisicing elit, sed do eiusmod tempor.</p></div>
<div class="abs special" style="top:182px;background:#3fbfcc"><h3>TODAY'S SPECIAL</h3><p>Lorem ipsum dolor sit amet, consectetur adipisicing elit, sed do eiusmod tempor.</p></div>
<div class="abs special" style="top:240px;background:#6fcdd5"><h3>COMBO PRODUCT</h3><p>Lorem ipsum dolor sit amet, consectetur adipisicing elit, sed do eiusmod tempor.</p></div>
<div class="abs special" style="top:297px;background:#8fd2d6"><h3>SPECIAL OFFERS</h3><p>Lorem ipsum dolor sit amet, consectetur adipisicing elit, sed do eiusmod tempor.</p></div>

<div class="abs heading" style="top:389px">Brand Name</div><div class="abs heading-rule" style="top:412px"></div>
<div class="abs heading" style="top:605px">Brand Name</div><div class="abs heading-rule" style="top:628px"></div>
<div class="abs heading" style="top:818px">Brand Name</div><div class="abs heading-rule" style="top:841px"></div>

<div class="abs card" style="left:78px;top:428px"><div class="shot" role="img" aria-label="Laptop product photo"></div><div class="base"></div></div>
<div class="abs card" style="left:187px;top:428px"><div class="shot" role="img" aria-label="Laptop product photo"></div><div class="base"></div></div>
<div class="abs card" style="left:296px;top:428px"><div class="shot" role="img" aria-label="Laptop product photo"></div><div class="base"></div></div>
<div class="abs card" style="left:404px;top:428px"><div class="shot" role="img" aria-label="Laptop product photo"></div><div class="base"></div></div>
<div class="abs meta" style="left:78px;top:538px">Specification<br>Features<br>Price</div>
<div class="abs meta" style="left:187px;top:538px">Specification<br>Features<br>Price</div>
<div class="abs meta" style="left:296px;top:538px">Specification<br>Features<br>Price</div>
<div class="abs meta" style="left:404px;top:538px">Specification<br>Features<br>Price</div>

<div class="abs card" style="left:78px;top:644px"><div class="shot" role="img" aria-label="Laptop product photo"></div><div class="base"></div></div>
<div class="abs card" style="left:187px;top:644px"><div class="shot" role="img" aria-label="Laptop product photo"></div><div class="base"></div></div>
<div class="abs card" style="left:296px;top:644px"><div class="shot" role="img" aria-label="Laptop product photo"></div><div class="base"></div></div>
<div class="abs card" style="left:404px;top:644px"><div class="shot" role="img" aria-label="Laptop product photo"></div><div class="base"></div></div>
<div class="abs meta" style="left:78px;top:754px">Specification<br>Features<br>Price</div>
<div class="abs meta" style="left:187px;top:754px">Specification<br>Features<br>Price</div>
<div class="abs meta" style="left:296px;top:754px">Specification<br>Features<br>Price</div>
<div class="abs meta" style="left:404px;top:754px">Specification<br>Features<br>Price</div>

<div class="abs card" style="left:78px;top:856px"><div class="shot" role="img" aria-label="Laptop product photo"></div><div class="base"></div></div>
<div class="abs card" style="left:187px;top:856px"><div class="shot" role="img" aria-label="Laptop product photo"></div><div class="base"></div></div>
<div class="abs card" style="left:296px;top:856px"><div class="shot" role="img" aria-label="Laptop product photo"></div><div class="base"></div></div>
<div class="abs card" style="left:404px;top:856px"><div class="shot" role="img" aria-label="Laptop product photo"></div><div class="base"></div></div>
<div class="abs meta" style="left:78px;top:966px">Specification<br>Features<br>Price</div>
<div class="abs meta" style="left:187px;top:966px">Specification<br>Features<br>Price</div>
<div class="abs meta" style="left:296px;top:966px">Specification<br>Features<br>Price</div>
<div class="abs meta" style="left:404px;top:966px">Specification<br>Features<br>Price</div>

<div class="abs side-h" style="top:389px">SPECIFICATIONAL CATEGORY</div>
<div class="abs side-bar" style="top:409px"></div>
<div class="abs specs">
  <span>Specification 1</span><span>Specification 1</span>
  <span>Specification 2</span><span>Specification 2</span>
  <span>Specification 3</span><span>Specification 3</span>
  <span>Specification 4</span><span>Specification 4</span>
  <span>Specification 5</span><span>Specification 5</span>
  <span>Specification 6</span><span>Specification 6</span>
  <span>Specification 7</span><span>Specification 7</span>
  <span>Specification 8</span><span>Specification 8</span>
  <span>Specification 9</span><span>Specification 9</span>
  <span>Specification 10</span><span>Specification 10</span>
</div>

<div class="abs side-h" style="top:672px">LATEST POSTS</div>
<div class="abs side-bar" style="top:690px"></div>
<div class="abs post" style="top:705px"><div class="thumb" role="img" aria-label="Post thumbnail"></div><p>Lorem ipsum dolor sit amet, consectetur adipisicing elit, sed do eiusmod tempor incididunt ut labore et dolore magna aliqua. Ut enim ad minim veniam, quis nostrud exercitation ullamco laboris nisi ut aliquip ex ea commodo consequat.</p></div>
<div class="abs post-rule" style="top:794px"></div>
<div class="abs post" style="top:808px"><div class="thumb" role="img" aria-label="Post thumbnail"></div><p>Lorem ipsum dolor sit amet, consectetur adipisicing elit, sed do eiusmod tempor incididunt ut labore et dolore magna aliqua. Ut enim ad minim veniam, quis nostrud exercitation ullamco laboris nisi ut aliquip ex ea commodo consequat.</p></div>
<div class="abs post-rule" style="top:902px"></div>
<div class="abs post" style="top:916px"><div class="thumb" role="img" aria-label="Post thumbnail"></div><p>Lorem ipsum dolor sit amet, consectetur adipisicing elit, sed do eiusmod tempor incididunt ut labore et dolore magna aliqua. Ut enim ad minim veniam, quis nostrud exercitation ullamco laboris nisi ut aliquip ex ea commodo consequat.</p></div>

<footer class="abs footer"></footer>
<div class="abs foot-h" style="left:84px;top:1041px">ABOUT</div>
<p class="abs about-p">Lorem ipsum dolor sit amet, consectetur adipiscing elit. Proin ut purus odio, quis rutrum nibh. Etiam nec tellus malesuada odio tincidunt fringilla quis vitae nisi. Lorem ipsum dolor sit amet, consectetur adipiscing elit. Nullam fringilla malesuada convallis. Morbi laoreet volutpat rhoncus.</p>
<div class="abs foot-h" style="left:378px;top:1041px">BROWSE</div>
<div class="abs links" style="left:378px;top:1066px">Link<br>Link<br>Link<br>Link<br>Link<br>Link</div>
<div class="abs links" style="left:464px;top:1066px">Home<br>About Me<br>Design Services<br>Request Quote<br>Advertise<br>Contact Me</div>
<div class="abs pay"><small>Payment Options</small><div class="badges"><span>Tellicard</span><span>Orvanta</span><span>Paylinko</span><span>Quillpass</span></div></div>
<div class="abs copy">Copyright Statement | Privacy Policy | Terms &amp; Conditions</div>
</body>
</html>
```